Donation Banner for Briarcrest High School Entrances

Create a banner to be hung at entrances at the school, to encourage participation in donation campaign.

See examples on attached document. What I like about the sampes: clean, easy to read, clear, mission-oriented.

Briarcrest Rd
Desired Size 100”w x 70”h

Castellan Rd Entrance
Desired Size 70”w x 50”h

Target Market(s)

Parents from the school and community members driving by. Silicon Valley professionals.

Font styles to use
Sans Serif

Colors
f78f20
9bcb3c
0393ce

Requirements
Must have
• School colors are orange and black. We can introduce small amounts of another color - maybe green to encourage donations. Or blue as it is opposite of orange on the color wheel.
• Banner must track dollar $$$ goal tracking up to $1.1M, in 200K increments (or whatever looks good) not %
• Our goal is 1.1M.
• Arrow Up, not thermometer.
• List website: bhsfoundation-example.org.
• Include round Briarcrest Foundation logo, see file provided.
• Must include mission oriented messaging: Reduced Class Sizes, Expanded Electives, Student Support
• Our Organization is Briarcrest High School Foundation, must be listed

```html
<!DOCTYPE html>
<html lang="en">
<head>
<meta charset="utf-8">
<title>Briarcrest High School Foundation – Donation Banner</title>
<link rel="stylesheet" href="https://fonts.googleapis.com/css2?family=Archivo+Black&family=Archivo:wght@700;800&family=Arimo:wght@400;700&family=PT+Serif:wght@700&display=swap">
<style>
  :root {
    --page-bg: #eceeef;
    --banner-orange: #fd4700;
    --band-orange: #ff4d0a;
    --arrow-tip: #ff5d24;
    --arrow-green: #7ab51f;
    --black: #000000;
    --white: #ffffff;
    --blue: #0a87c9;
    --grey-text: #555555;
    --rule: #f5875c;
    --org-red: #f2440f;
    --web-green: #6aaa1e;
  }
  * { box-sizing: border-box; margin: 0; padding: 0; }
  html, body {
    width: 1200px; height: 928px; overflow: hidden;
    background: var(--page-bg);
  }
  .banner {
    position: absolute; left: 0; top: 45px;
    width: 1200px; height: 838px;
    background: var(--white);
  }
  .goal-panel {
    position: absolute; left: 0; top: 0;
    width: 600px; height: 823px;
    background: var(--banner-orange);
  }
  .goal-header {
    position: absolute; left: 0; top: 43px;
    width: 600px; height: 114px;
    background: var(--black);
    color: var(--white);
    text-align: center;
  }
  .goal-title {
    font-family: "Archivo Black", sans-serif;
    font-size: 42px; line-height: 1;
    letter-spacing: 1px;
    margin-top: 17px;
  }
  .goal-subtitle {
    font-family: "Arimo", sans-serif;
    font-size: 26px; letter-spacing: 6px;
    margin-top: 12px;
  }
  .goal-arrow { position: absolute; left: 0; top: 0; }
  .amount {
    position: absolute; left: 339px;
    font-family: "PT Serif", serif; font-weight: 700;
    color: var(--white); font-size: 24px; line-height: 1;
    display: flex; align-items: center; gap: 10px;
    transform: translateY(-50%);
  }
  .amount::before {
    content: ""; width: 17px; height: 1.5px; background: var(--white);
  }
  .amount-goal {
    left: 262px; font-size: 33px; gap: 16px;
  }
  .amount-goal::before { width: 24px; }
  .amount-goal::after {
    content: ""; width: 24px; height: 1.5px; background: var(--white);
  }
  .message-panel {
    position: absolute; left: 600px; top: 0;
    width: 600px; height: 823px;
    text-align: center;
  }
  .you {
    position: absolute; left: 0; width: 600px; top: 66px;
    font-family: "Archivo Black", sans-serif;
    font-size: 50px; line-height: 1; color: var(--black);
  }
  .difference {
    position: absolute; left: 0; width: 600px; top: 125px;
    font-family: "Archivo", sans-serif; font-weight: 800;
    font-size: 29px; line-height: 1; color: var(--blue);
    letter-spacing: 0.5px;
  }
  .funds-heading {
    position: absolute; left: 0; width: 600px; top: 277px;
    font-family: "Arimo", sans-serif; font-size: 21px;
    color: var(--grey-text);
  }
  .funds-rule {
    position: absolute; left: 51px; top: 311px;
    width: 498px; height: 1px; background: var(--rule);
  }
  .funds-list {
    position: absolute; left: 0; width: 600px; top: 326px;
    font-family: "Arimo", sans-serif; font-weight: 700;
    font-size: 22px; line-height: 30px; color: var(--black);
  }
  .foundation-mark {
    position: absolute; left: 221px; top: 506px;
    width: 158px; height: 158px; border-radius: 50%;
    border: 4px solid var(--black);
    display: flex; align-items: center; justify-content: center;
    font-family: "Arimo", sans-serif; font-weight: 700;
    font-size: 17px; line-height: 22px; color: var(--org-red);
    letter-spacing: 1px;
  }
  .org-name {
    position: absolute; left: 0; width: 600px; top: 700px;
    font-family: "Arimo", sans-serif; font-weight: 700;
    font-size: 22px; color: var(--org-red);
  }
  .org-web {
    position: absolute; left: 0; width: 600px; top: 740px;
    font-family: "Arimo", sans-serif; font-size: 21px;
    color: var(--web-green);
  }
  .base-bar {
    position: absolute; left: 0; top: 823px;
    width: 1200px; height: 15px; background: var(--black);
  }
  .top-band {
    position: absolute; left: 0; top: 0; width: 600px; height: 43px;
    background: var(--band-orange);
  }
</style>
</head>
<body>
  <main class="banner">
    <section class="goal-panel">
      <div class="top-band"></div>
      <header class="goal-header">
        <h1 class="goal-title">HELP US</h1>
        <p class="goal-subtitle">TO REACH OUR GOAL</p>
      </header>
      <svg class="goal-arrow" width="600" height="823" viewBox="0 0 600 823" aria-hidden="true">
        <polygon points="192,211 277,289 239,289 239,765 144,765 144,289 107,289"
                 fill="var(--arrow-green)" stroke="var(--white)" stroke-width="2" stroke-linejoin="miter"/>
        <polygon points="192,212.5 264,278 120,278" fill="var(--arrow-tip)"/>
      </svg>
      <div class="amount amount-goal" style="top:227px">$1,100,000</div>
      <div class="amount" style="top:332px">$900,000</div>
      <div class="amount" style="top:438px">$700,000</div>
      <div class="amount" style="top:543px">$500,000</div>
      <div class="amount" style="top:649px">$300,000</div>
      <div class="amount" style="top:754px">$100,000</div>
    </section>

    <section class="message-panel">
      <h2 class="you">YOU</h2>
      <p class="difference">MAKE THE DIFFERENCE</p>
      <p class="funds-heading">Where the Money Goes</p>
      <div class="funds-rule"></div>
      <p class="funds-list">Reduced Class Sizes | Expanded Electives<br>Student Support</p>
      <div class="foundation-mark">BRIARCREST<br>FOUNDATION</div>
      <p class="org-name">BRIARCREST HIGH SCHOOL FOUNDATION</p>
      <p class="org-web">www.bhsfoundation-example.org</p>
    </section>

    <div class="base-bar"></div>
  </main>
</body>
</html>
```